Dance school needs a poster to promote our annual concert

I have a dance school called 'The Marcella Dunwoody Dancers'
See designs from previous years
This year's concert theme is Brant Holloway animation movies
The title of the concert is "glimmeRa"
Dance items will be choreographed to; “Quiet Orchard”, Copper Heron”, “The Nine Lanterns”, “The Fox Regent”, “Temrik”, “Willow & the Warden” & “Pipsqueeve”.
I need a colorful A4 (portrait) poster promoting the concert.

Target Market(s)

Families of students & dance community

Industry/Entity Type

Dance Studio

Font styles to use
Other font styles liked:
• "Mistral" for my my name (see examples supplied)

Colors

Designer to choose colors to be used in the design.

Requirements
Must have
• Must Have:
• - The poster must include the following information:
• 'The Marcella Dunwoody Dancers'
• presents
• "glimmeRa"
• (Font for my name is "Mistral")
• Saturday 18th November 2017
• Corbett Hall,
• Halverd Grammar Elmstead.

```html
<!DOCTYPE html>
<html lang="en">
<head>
<meta charset="utf-8">
<title>glimmeRa – The Marcella Dunwoody Dancers</title>
<link rel="stylesheet" href="https://fonts.googleapis.com/css2?family=Baloo+2:wght@800&family=Dancing+Script:wght@600&family=Oswald:wght@500&family=Roboto+Slab:wght@600;700&display=swap">
<style>
  :root {
    --page-bg: #ececea;
    --sky-top: #1c2461;
    --sky-mid: #223b7a;
    --night-floor: #1d1719;
    --gold-light: #fff36a;
    --gold-deep: #f2a900;
    --title-edge: #3a1f6e;
    --band-purple: #2e2163;
    --band-text: #ffe94a;
    --ink-white: #ffffff;
  }
  * { margin: 0; padding: 0; box-sizing: border-box; }
  html, body {
    width: 1200px; height: 1039px; overflow: hidden;
    background: var(--page-bg);
  }
  .poster {
    position: absolute; left: 250px; top: 20px;
    width: 700px; height: 998px; overflow: hidden;
    background: linear-gradient(180deg, var(--sky-top) 0%, var(--sky-mid) 45%, #1f3165 62%, var(--night-floor) 82%, var(--night-floor) 100%);
    color: var(--ink-white);
    text-align: center;
  }
  .studio-mark {
    position: absolute; top: 58px; left: 0; width: 100%;
    display: flex; justify-content: center; align-items: center; gap: 10px;
    font-family: "Roboto Slab", serif; font-weight: 700; font-size: 30px;
    letter-spacing: 3px; color: var(--ink-white);
  }
  .studio-mark .dot {
    width: 14px; height: 14px; border-radius: 50%; background: var(--ink-white);
  }
  .studio-name {
    position: absolute; top: 148px; left: 0; width: 100%;
    font-family: "Dancing Script", cursive; font-weight: 600; font-size: 38px;
    white-space: nowrap;
  }
  .presents {
    position: absolute; top: 218px; left: 0; width: 100%;
    font-family: "Roboto Slab", serif; font-weight: 700; font-size: 24px;
  }
  .show-title {
    position: absolute; top: 262px; left: 0; width: 100%;
    font-family: "Baloo 2", sans-serif; font-weight: 800; font-size: 112px;
    line-height: 1; letter-spacing: -2px;
  }
  .show-title svg { display: block; margin: 0 auto; overflow: visible; }
  .scene-photo {
    position: absolute; top: 420px; left: 0; width: 100%; height: 400px;
    background:
      radial-gradient(ellipse 40% 35% at 50% 55%, rgba(214,70,50,0.85), rgba(214,70,50,0) 70%),
      radial-gradient(ellipse 60% 18% at 50% 80%, rgba(230,150,70,0.45), rgba(230,150,70,0) 70%),
      linear-gradient(180deg, rgba(35,59,120,0) 0%, rgba(35,59,120,0.4) 30%, #3a2624 75%, var(--night-floor) 100%);
  }
  .date-band {
    position: absolute; top: 788px; left: 50%; transform: translateX(-50%);
    height: 52px; padding: 0 14px;
    background: var(--band-purple);
    font-family: "Oswald", sans-serif; font-weight: 500; font-size: 29px;
    line-height: 52px; color: var(--band-text); letter-spacing: 0.3px;
    white-space: nowrap;
  }
  .venue {
    position: absolute; top: 866px; left: 0; width: 100%;
    font-family: "Roboto Slab", serif; font-weight: 600; font-size: 25px; line-height: 34px;
  }
</style>
</head>
<body>
  <main class="poster">
    <div class="studio-mark"><span>MDD</span><span class="dot"></span></div>
    <p class="studio-name">The Marcella Dunwoody Dancers</p>
    <p class="presents">Presents</p>
    <h1 class="show-title">
      <svg width="520" height="130" viewBox="0 0 520 130" aria-label="glimmeRa">
        <defs>
          <linearGradient id="title-gold" x1="0" y1="0" x2="0" y2="1">
            <stop offset="0" stop-color="#fff36a"/>
            <stop offset="1" stop-color="#f2a900"/>
          </linearGradient>
        </defs>
        <text x="260" y="95" text-anchor="middle" fill="url(#title-gold)" stroke="#3a1f6e" stroke-width="10" paint-order="stroke" stroke-linejoin="round">glimmeRa</text>
      </svg>
    </h1>
    <div class="scene-photo" role="img" aria-label="Illuminated fairy-tale castle with red-lit towers at dusk, fountain plaza in front"></div>
    <div class="date-band">SATURDAY 18TH NOVEMBER 2017</div>
    <p class="venue">Corbett Hall<br>Halverd Grammar Elmstead</p>
  </main>
</body>
</html>
```